Business card design needed

Family General Practitioner/ Family Physician.
Logo is the logo of the Crestmoor Guild of Family Clinicians Australia
http://kvplm.tarevo.edu.au/PictureGallery/logos/pages/CGFC%20logo_jpg.htm

Reason: Just a bit more time to make changes and the weekend for me to look at things closely and to choose. Thanks, Lumi

Thanks for all the submissions. So many of them are really works of art. Not one of them are not good. The ones that I am eliminating are the ones that I think are not suitable for me personally only, and because if I don't, it makes it very difficult to decide as many of you are also sending me slight variations of a card. I have just decided to choose a second place card too. Can't thank you all enough. Good luck, Lumi. P.S - Working today till 10 pm as the card says :-), so probably won't be able to give a feedback till late Saturday night or Sunday morning here in Sydney, Australia. 

Reason: Just added a second place to the budget and realised that Australia is ahead of the rest of the world in the time zone (only :-) - don't want to offend anyone or start a debate!! ) , so Monday deadline will mean it will be a weekend for the rest of the world. Just wanted to give everyone more time to submit their best, especially since I will be picking a second card too. Can't thank everyone enough for the submissions. P.S - Not keen on photos on the card.

Contact Information for Business Card

Dr. Lumi Harcourt M.B.B.S., F.C.G.F.C
Family General Practitioner
Address, timings, phone and fax number on the back.

Requirements
Must have
• Timings
Mon 7 am - 7 pm
Tues 7 am - 12 pm
Wed 7 am - 10 pm
Thurs 7 am - 12 pm
Fri 7 am - 8 pm
Sat 8 am - 10 pm
Sun - Off

```html
<!DOCTYPE html>
<html lang="en">
<head>
<meta charset="utf-8">
<title>Dr Lumi Harcourt – Business Card</title>
<link rel="stylesheet" href="https://fonts.googleapis.com/css2?family=Arimo:wght@400;700&display=swap">
<style>
  :root{
    --navy:#1f3088;
    --navy-deep:#17246e;
    --red:#c8102e;
    --cream:#fbf6dc;
    --ink:#1a1a22;
    --stage:#e9e7e3;
  }
  *{box-sizing:border-box;margin:0;padding:0}
  html,body{width:1200px;height:716px;overflow:hidden;background:var(--stage)}
  body{font-family:"Arimo",Arial,sans-serif;position:relative}
  .card{position:absolute;top:193px;width:560px;height:330px;background:var(--navy);overflow:hidden;box-shadow:0 6px 18px rgba(0,0,0,.25)}
  .card--front{left:30px}
  .card--back{left:610px}

  /* front */
  .front-glow{position:absolute;left:60px;top:-20px;width:300px;height:260px;border-radius:50%;
    background:radial-gradient(closest-side,rgba(255,255,255,.75),rgba(170,180,230,.35) 55%,rgba(31,48,136,0) 100%)}
  .front-band{position:absolute;left:0;right:0;top:150px;height:30px;background:var(--red)}
  .front-band::after{content:"";position:absolute;left:0;right:0;top:9px;height:12px;background:var(--cream)}
  .doctor-name{position:absolute;left:190px;top:84px;font-size:17px;color:var(--ink)}
  .credentials{position:absolute;left:170px;top:112px;padding:3px 14px;background:var(--cream);border:3px solid var(--red);
    color:var(--red);font-weight:700;font-size:18px;letter-spacing:.5px}
  .specialty{position:absolute;left:40px;top:184px;padding:4px 14px;background:var(--red);border:3px solid var(--cream);
    color:var(--cream);font-weight:700;font-size:25px}
  .college-mark{position:absolute;left:400px;top:92px;display:flex;align-items:center;gap:8px;
    color:var(--cream);font-weight:700;font-size:22px}
  .college-mark .dot{width:30px;height:30px;border-radius:50%;background:var(--cream)}

  /* back */
  .hours{position:absolute;left:0;top:12px;width:100%}
  .day-row{position:relative;height:30px}
  .day-row .stripe{position:absolute;top:4px;height:22px;background:var(--red);border-top:2px solid var(--cream);border-bottom:2px solid var(--cream)}
  .day-row .day{position:absolute;top:7px;color:var(--cream);font-weight:700;font-size:14px}
  .day-row .time{position:absolute;top:7px;height:17px;width:190px;background:var(--cream);border:2px solid var(--red);
    color:var(--red);font-weight:700;font-size:13px;line-height:13px;padding-left:10px}
  .day-row--left .stripe{left:0;width:78%}
  .day-row--left .day{left:18px}
  .day-row--left .time{left:150px}
  .day-row--right .stripe{right:0;width:78%}
  .day-row--right .day{right:24px}
  .day-row--right .time{right:150px}
  .contact{position:absolute;left:10px;right:10px;bottom:10px;height:84px;background:var(--red);border:4px solid var(--cream);
    color:var(--cream);font-weight:700;font-size:14px;padding:10px 16px;display:flex;justify-content:space-between;line-height:1.35}
  .contact .phones{align-self:flex-end;text-align:left}
</style>
</head>
<body>
  <section class="card card--front" aria-label="Business card front">
    <div class="front-glow"></div>
    <div class="front-band"></div>
    <p class="doctor-name">Dr Lumi Harcourt</p>
    <p class="credentials">M.B.B.S.&amp; F.C.G.F.C</p>
    <p class="specialty">Family General Practitioner</p>
    <div class="college-mark"><span class="dot"></span>CGFC</div>
  </section>

  <section class="card card--back" aria-label="Business card back">
    <div class="hours">
      <div class="day-row day-row--left"><span class="stripe"></span><span class="day">Monday</span><span class="time">7am - 7pm</span></div>
      <div class="day-row day-row--right"><span class="stripe"></span><span class="day">Tuesday</span><span class="time">7am - 12pm</span></div>
      <div class="day-row day-row--left"><span class="stripe"></span><span class="day">Wednesday</span><span class="time">7am - 10pm</span></div>
      <div class="day-row day-row--right"><span class="stripe"></span><span class="day">Thursday</span><span class="time">7am - 12pm</span></div>
      <div class="day-row day-row--left"><span class="stripe"></span><span class="day">Friday</span><span class="time">7am - 8pm</span></div>
      <div class="day-row day-row--right"><span class="stripe"></span><span class="day">Saturday</span><span class="time">8am - 10pm</span></div>
      <div class="day-row day-row--left"><span class="stripe"></span><span class="day">Sunday</span><span class="time">Off</span></div>
    </div>
    <div class="contact">
      <p class="address">Upper Level, Juniper Court, Larkfield Square Shopping Centre<br>Brookvale Ridge, NSW 2198</p>
      <p class="phones">Phone: 02 5550 1840<br>Fax: 02 5550 1877</p>
    </div>
  </section>
</body>
</html>
```